Business Card Design - Photographer

I am a landscape photographer and I require a business card design. 

I require two designs:
1)  a double sided business card
 and
b)  a single sided business card 

The single sided design can either be the same as the double sided (with just one side having all the information)....or it can be an entire new design. Its up to you.

My corporate colours are (CMYK):

Blue   69, 32, 0, 0
Grey  72,  64,  47,  31
Green  32,  2,  91,  0
Yellow   0, 19, 92, 0
Orange  0, 39, 75, 0

Colour space in final file should be in CMYK.

The details that need to be included on the card:

- Use the provided Logo
- Name: Lukas Wendrovski
- Email:   sales@vistaplume.com.au
- Website:    vistaplume.com.au
- Twitter:    twitter.com/vistaplume
- Facebook:   facebook.com/vistaplume
- Mobile  0415 309 662

Please use the attached template to design the logo to the specified size, including the marked bleed lines. I have also attached my logo in PNG (transparent background) and ai format for you to use.

The final file should be:
- Photoshop version with layers so I can edit the name/text etc. All non vector files should be high resolution at 1039 x 697 pixels at 300 dpi.

I also require a file as:
- Vector based PDF

Anyway questions please contact me.

Thank you

Industry/Entity Type

Landscape

Logo styles of interest
Pictorial/Combination Logo
Abstract Logo
Wordmark Logo
Lettermark Logo
Requirements
Must have
• The details that need to be included on the card:

- Use the provided Logo
- Name: Lukas Wendrovski
- Email: sales@vistaplume.com.au
- Website: vistaplume.com.au
- Twitter: twitter.com/vistaplume
- Facebook: facebook.com/vistaplume
- Mobile 0415 309 662

```html
<!DOCTYPE html>
<html lang="en">
<head>
<meta charset="utf-8">
<title>Vista Plume – Business Cards</title>
<link rel="stylesheet" href="https://fonts.googleapis.com/css2?family=Cinzel:wght@500&family=Bebas+Neue&display=swap">
<style>
  :root {
    --backdrop: #b9b9b9;
    --paper: #ffffff;
    --brand-blue: #3f8fd0;
    --brand-grey: #363b4c;
    --brand-green: #a9c938;
    --brand-yellow: #fdcb1e;
    --brand-orange: #f6a547;
  }
  * { box-sizing: border-box; margin: 0; padding: 0; }
  html, body { width: 1200px; height: 800px; overflow: hidden; }
  body {
    background: var(--backdrop);
    position: relative;
    font-family: "Bebas Neue", "Arial Narrow", sans-serif;
  }
  .card {
    position: absolute;
    top: 219px;
    width: 540px;
    height: 362px;
    background: var(--paper);
    overflow: hidden;
  }
  .card--front { left: 40px; }
  .card--back { left: 620px; }

  .brand {
    display: flex;
    align-items: center;
    gap: 10px;
    font-family: "Cinzel", "Times New Roman", serif;
    font-weight: 500;
    color: var(--brand-grey);
    white-space: nowrap;
  }
  .brand__dot {
    border-radius: 50%;
    background: var(--brand-grey);
    flex: none;
  }

  .card--front .brand {
    position: absolute;
    left: 0; right: 0; top: 150px;
    justify-content: center;
    font-size: 34px;
    letter-spacing: 1px;
  }
  .card--front .brand__dot { width: 26px; height: 26px; }
  .front-swoosh {
    position: absolute;
    left: 0; bottom: 0;
    width: 540px; height: 60px;
  }

  .card--back .brand {
    position: absolute;
    left: 34px; top: 34px;
    font-size: 18px;
  }
  .card--back .brand__dot { width: 16px; height: 16px; }

  .details {
    position: absolute;
    left: 34px;
    bottom: 40px;
    padding-left: 14px;
    border-left: 7px solid var(--brand-yellow);
    line-height: 1;
  }
  .details__role { color: var(--brand-green); font-size: 22px; }
  .details__name { font-size: 46px; color: var(--brand-grey); margin-top: 2px; }
  .details__first { color: var(--brand-blue); }
  .details__line {
    font-size: 16px;
    color: var(--brand-grey);
    margin-top: 4px;
    white-space: nowrap;
  }
  .details__line .note { color: var(--brand-blue); }
  .details__rule {
    height: 1px;
    background: var(--brand-grey);
    width: 440px;
    margin-top: 4px;
  }
  .details__line--web { color: var(--brand-green); }
  .details__line--web .sep { color: var(--brand-grey); }
</style>
</head>
<body>

  <section class="card card--front" aria-label="Card front">
    <div class="brand"><span class="brand__dot"></span>Vista Plume</div>
    <svg class="front-swoosh" viewBox="0 0 540 60" preserveAspectRatio="none" aria-hidden="true">
      <path d="M0 60 L0 52 C200 46 380 30 540 0 L540 60 Z" fill="var(--brand-blue)"/>
    </svg>
  </section>

  <section class="card card--back" aria-label="Card back">
    <div class="brand"><span class="brand__dot"></span>Vista Plume</div>
    <div class="details">
      <p class="details__role">Art Photography</p>
      <p class="details__name"><span class="details__first">Lukas</span> Wendrovski</p>
      <p class="details__line">0415 309 662 <span class="note">[Mobile]</span> &nbsp;|&nbsp; vistaplume <span class="note">[Social]</span></p>
      <div class="details__rule"></div>
      <p class="details__line details__line--web">sales@vistaplume.com.au <span class="sep">&nbsp;|&nbsp;</span> www.vistaplume.com.au</p>
    </div>
  </section>

</body>
</html>
```